Velvet Dare Age Verification Landing Page

To create a visually appealing design for the landing page of the adult game "Velvet Dare" that confirms the visitor's age.
The design should have a simple and visually appealing look that focuses on two buttons labeled "Yes" and "No". The purpose of the page is to confirm that the visitor is 18 years of age or older before accessing the game's content. Responsive design that works well on desktop and mobile devices. The final output should be delivered in PSD, AI, or Sketch format, along with any necessary images or assets.
I have also attached examples.

```html
<!DOCTYPE html>
<html lang="en">
<head>
<meta charset="utf-8">
<title>Velvet Dare — Age Verification</title>
<link href="https://fonts.googleapis.com/css2?family=Roboto:wght@400;500;700&display=swap" rel="stylesheet">
<style>
  :root {
    --bg-deep: #1a1310;
    --bg-warm: #3a2c25;
    --bg-light: #5a4c47;
    --panel: rgba(12, 10, 10, 0.72);
    --text: #ffffff;
    --brand: #9a5cc2;
    --button: #0a6fbd;
    --check: #ffffff;
  }
  * { margin: 0; padding: 0; box-sizing: border-box; }
  html, body {
    width: 1200px;
    height: 786px;
    overflow: hidden;
    font-family: "Roboto", Arial, sans-serif;
    color: var(--text);
    background: var(--bg-deep);
  }
  .page {
    position: relative;
    width: 1200px;
    height: 786px;
    overflow: hidden;
  }
  .hero-photo {
    position: absolute;
    inset: 0;
    background:
      radial-gradient(ellipse 420px 300px at 560px 300px, rgba(120, 95, 80, 0.45), transparent 70%),
      radial-gradient(ellipse 500px 260px at 950px 240px, rgba(110, 100, 100, 0.35), transparent 70%),
      radial-gradient(ellipse 700px 240px at 500px 720px, rgba(140, 135, 135, 0.45), transparent 70%),
      linear-gradient(180deg, var(--bg-deep) 0%, var(--bg-warm) 45%, var(--bg-light) 100%);
  }
  .age-gate {
    position: absolute;
    left: 306px;
    top: 200px;
    width: 588px;
    height: 386px;
    background: var(--panel);
    text-align: center;
  }
  .brand {
    position: absolute;
    left: 0;
    right: 0;
    top: 62px;
    display: flex;
    align-items: center;
    justify-content: center;
    gap: 12px;
  }
  .brand-dot {
    width: 22px;
    height: 22px;
    border-radius: 50%;
    background: var(--text);
  }
  .brand-name {
    font-size: 38px;
    font-weight: 700;
    color: var(--brand);
    letter-spacing: 0.5px;
  }
  .age-question {
    position: absolute;
    left: 0;
    right: 0;
    top: 178px;
    font-size: 26px;
    font-weight: 700;
  }
  .choices {
    position: absolute;
    left: 161px;
    top: 245px;
    display: flex;
    gap: 9px;
  }
  .choice {
    width: 129px;
    height: 55px;
    border: none;
    border-radius: 2px;
    background: var(--button);
    color: var(--text);
    font-family: "Roboto", Arial, sans-serif;
    font-size: 25px;
    font-weight: 500;
  }
  .remember {
    position: absolute;
    left: 209px;
    top: 325px;
    display: flex;
    align-items: center;
    gap: 14px;
    font-size: 20px;
  }
  .remember-box {
    width: 19px;
    height: 19px;
    border-radius: 4px;
    background: var(--check);
  }
</style>
</head>
<body>
  <main class="page">
    <div class="hero-photo" role="img" aria-label="Dimly lit photograph of a woman in black lingerie reclining on a bed with white sheets"></div>

    <section class="age-gate">
      <div class="brand">
        <span class="brand-dot"></span>
        <span class="brand-name">Velvet Dare</span>
      </div>
      <h1 class="age-question">Are You over 18 years of age?</h1>
      <div class="choices">
        <button class="choice choice-yes">Yes</button>
        <button class="choice choice-no">No</button>
      </div>
      <label class="remember">
        <span class="remember-box"></span>
        <span class="remember-label">Remember Me</span>
      </label>
    </section>
  </main>
</body>
</html>
```